Business cards to launch an education platform

Hi,
I am looking at having new business cards designed.
I am a startup, developing a web platform for schools and university, the education world. It's an online assessment system.
I would like a card that looks classy, and that is using the colors and the font of my logo.

I have attached:
1) my logo
2) A business card that I have designed quickly so you can have all the information required in the card, but I really don't like it.
3) The font that I am using (Lato Regular) to design my web platform
4) Some screenshots of my web platform so you can have a look at the style that I have.

Target Market(s)

Major market: Education system: Schools and university
Minor markets: Business in general

Industry/Entity Type

Business

Contact Information for Business Card

Lydia Marsh
Director

M: 0437 681 902
E: lydia.marsh@copperLeafSystems.com.au

Requirements
Must have
• The colors of my logo

```html
<!DOCTYPE html>
<html lang="en">
<head>
<meta charset="utf-8">
<title>Copper Leaf Systems – Business Card</title>
<link href="https://fonts.googleapis.com/css2?family=Lato:wght@400;700&display=swap" rel="stylesheet">
<style>
  :root{
    --page:#ecebe8;
    --card-white:#ffffff;
    --card-shade:#eef0f2;
    --blue-deep:#135a9c;
    --blue-mid:#1f74b8;
    --blue-light:#2c86c8;
    --cyan:#2fc6e8;
    --steel:#2d6ea8;
    --ink:#1a1a1a;
  }
  *{box-sizing:border-box;margin:0;padding:0}
  html,body{width:1200px;height:892px;overflow:hidden}
  body{background:var(--page);font-family:"Lato",sans-serif;position:relative}

  .card{position:absolute;width:620px;height:354px;border-radius:4px;overflow:hidden;
        box-shadow:0 6px 18px rgba(0,0,0,.18)}
  .card--front{left:290px;top:64px;background:linear-gradient(135deg,var(--card-white) 55%,var(--card-shade))}
  .card--back{left:290px;top:472px;
        background:linear-gradient(160deg,var(--blue-light),var(--blue-mid) 45%,var(--blue-deep))}

  /* front */
  .front__band{position:absolute;left:0;top:0;width:140px;height:100%;
        background:linear-gradient(180deg,var(--blue-light),var(--blue-deep))}
  .front__rule{position:absolute;left:146px;top:0;width:4px;height:100%;background:var(--cyan)}
  .front__mark{position:absolute;left:92px;top:44px;width:96px;height:96px;
        background:var(--blue-mid);border:4px solid var(--card-white)}
  .front__company{position:absolute;left:210px;top:74px;font-size:30px;font-weight:400;
        letter-spacing:3px;text-transform:uppercase;color:var(--steel)}
  .front__name{position:absolute;left:210px;top:168px;font-size:32px;font-weight:700;
        color:var(--blue-mid);word-spacing:10px}
  .front__title{position:absolute;left:210px;top:206px;font-size:22px;font-weight:700;color:var(--ink)}
  .front__contact{position:absolute;left:210px;top:254px;list-style:none;
        font-size:17px;color:var(--ink);line-height:32px}
  .front__contact li{display:flex;align-items:center;gap:12px}
  .contact-icon{width:18px;height:18px;flex:none}

  /* back */
  .back__mark{position:absolute;left:278px;top:70px;width:64px;height:64px;border:5px solid var(--card-white)}
  .back__company{position:absolute;left:0;top:168px;width:100%;text-align:center;
        font-size:40px;font-weight:400;letter-spacing:5px;text-transform:uppercase;color:var(--card-white)}
</style>
</head>
<body>
  <section class="card card--front" aria-label="Business card front">
    <div class="front__band"></div>
    <div class="front__rule"></div>
    <div class="front__mark"></div>
    <p class="front__company">Copper Leaf Systems</p>
    <h1 class="front__name">Lydia Marsh</h1>
    <p class="front__title">Director</p>
    <ul class="front__contact">
      <li>
        <svg class="contact-icon" viewBox="0 0 18 18" aria-hidden="true">
          <rect width="18" height="18" fill="#1a1a1a"/>
          <path d="M5 4h2.5l1 3-1.5 1a7 7 0 0 0 3 3l1-1.5 3 1V13a1 1 0 0 1-1 1A9 9 0 0 1 4 5a1 1 0 0 1 1-1z" fill="#fff"/>
        </svg>
        <span>0437 681 902</span>
      </li>
      <li>
        <svg class="contact-icon" viewBox="0 0 18 18" aria-hidden="true">
          <rect width="18" height="18" fill="#1a1a1a"/>
          <rect x="3.5" y="5" width="11" height="8" fill="none" stroke="#fff" stroke-width="1.2"/>
          <path d="M3.5 5l5.5 4.5L14.5 5" fill="none" stroke="#fff" stroke-width="1.2"/>
        </svg>
        <span>lydia.marsh@copperLeafSystems.com.au</span>
      </li>
    </ul>
  </section>

  <section class="card card--back" aria-label="Business card back">
    <div class="back__mark"></div>
    <p class="back__company">Copper Leaf Systems</p>
  </section>
</body>
</html>
```